Jobinserat Vorlage medizinischer Bereich
Sehr gute Kommunikation auch mit Rückfragen damit das Projekt komplett verstanden wurde. Schnelle Umsetzung mit tollen Vorschlägen. Nur zu empfehlen!
Zielgruppe
Personalagentur im medizinischen Bereich (Krankenpfleger/Fachärzte)
Zielgruppe: Jobsuchende Krankenpflege Fachleute in Deutschland für die Schweiz!
Aufgabenstellung
jung, frisch, emotionell, verlockend
Bitte Text beachten: klinikpflegeleiterin
Wir benötigen ein Layout für ein Stelleninserat welches wir auf bei www.pflegestellenboerse.de platzieren möchten sowie auf www.medizinerkarriere.de / Das Format wird A4 sein, entweder eine oder zwei Seiten, je nachdem was für eine Stelle wir ausschreiben. Wichtig ist das Logo und der Text (siehe Projektanlage). Als Anhaltspunkt geht das Inserat (http://www.pflegestellenboerse.de/job/dipl-pflegefachfraudipl-pflegefachmann-hffh-oder-fage-fur-kurzeinsatze-10-20) in die Richtige Richtung, einfach mit unserer Farbe vom Logo oder der Academy http://www.valorintgruppe.com/academy/

```html
<!DOCTYPE html>
<html lang="de">
<head>
<meta charset="utf-8">
<title>Stelleninserat Klinikpflegeleitung</title>
<link rel="stylesheet" href="https://fonts.googleapis.com/css2?family=Source+Sans+3:wght@400;600;700&display=swap">
<style>
  :root{
    --stage:#ffffff;
    --paper:#ffffff;
    --amber:#e8a21c;
    --crimson:#b01c2a;
    --ink:#2d2d2d;
    --grey:#5a5a5a;
    --footer:#4a4a4a;
    --photo-top:#dfeef3;
    --photo-bottom:#c9d6da;
  }
  *{margin:0;padding:0;box-sizing:border-box}
  html,body{width:1200px;height:1200px;overflow:hidden;background:var(--stage)}
  body{font-family:"Source Sans 3",Arial,sans-serif;color:var(--ink)}
  .page{position:absolute;left:242px;top:95px;width:716px;height:1010px;background:var(--paper);border:1px solid #d6d6d6}
  .hero{position:absolute;left:0;top:0;width:631px;height:288px;
    background:linear-gradient(180deg,var(--photo-top) 0%,#eef3f4 45%,var(--photo-bottom) 100%)}
  .band{position:absolute;left:0;top:288px;width:631px;height:74px;background:var(--amber)}
  .band h1{position:absolute;left:60px;top:6px;font-size:45px;font-weight:600;color:#fff;letter-spacing:-.5px}
  .job-title{position:absolute;left:60px;top:377px;font-size:27px;font-weight:700;color:var(--crimson);letter-spacing:-.2px}
  .col{position:absolute;top:430px}
  .col.tasks{left:60px;width:285px}
  .col.reqs{left:360px;width:290px}
  .col h2{font-size:14px;font-weight:700;margin-bottom:10px}
  .col ul{list-style:none}
  .col li{position:relative;padding-left:16px;font-size:12px;line-height:15px;margin-bottom:5px}
  .col li::before{content:"";position:absolute;left:0;top:4px;width:6px;height:6px;background:var(--crimson)}
  .closing{position:absolute;left:60px;top:752px;width:600px;font-size:12.5px;line-height:15px}
  .closing p{margin-bottom:9px}
  .closing strong{font-weight:700}
  .advisor{position:absolute;left:60px;top:880px;font-size:12px;line-height:15px}
  .advisor h3{font-size:12px;font-weight:700;margin-bottom:7px}
  .advisor .social{margin-top:14px}
  .brand{position:absolute;left:418px;top:902px}
  .brand .name{display:flex;align-items:center;gap:8px;font-size:23px;font-weight:600;color:var(--amber);letter-spacing:1px}
  .brand .name span.dot{width:12px;height:12px;background:var(--amber);display:inline-block}
  .brand .address{margin-top:8px;font-size:8.5px;line-height:10px;color:var(--ink)}
  .page-foot{position:absolute;left:0;bottom:0;width:100%;height:7px;background:var(--footer)}
</style>
</head>
<body>
<div class="page">
  <div class="hero" role="img" aria-label="Foto: vier junge Pflegefachfrauen in weissen Kitteln mit Stethoskop in heller Klinikumgebung"></div>
  <div class="band"><h1>Wir suchen</h1></div>

  <div class="job-title">Klinikpflegeleiterin / Klinikpflegeleiter</div>

  <section class="col tasks">
    <h2>Ihre Aufgaben:</h2>
    <ul>
      <li>Sicherstellung einer wirksamen, wirtschaftlichen und zweckmässigen Pflege und Betreuung</li>
      <li>Führung und Förderung der unterstellten Mitarbeitenden inklusive Stellenplanbewirt­schaftung</li>
      <li>Mitwirkung bei der strategischen Weiterent­wicklung von unternehmensweiten Projekten und Kliniken</li>
      <li>Gewährleistung des Ausbildungsauftrages auf der Grund- und Tertiärstufe</li>
      <li>Qualitätssicherung und Prozessoptimierung gemäss der Unternehmensstrategie</li>
    </ul>
  </section>

  <section class="col reqs">
    <h2>Anfoderungen:</h2>
    <ul>
      <li>Dipl. Pflegefachfrau / -mann HF, DN II,<br>AKP, FH, DGKS</li>
      <li>Fundierte Führungserfahrung mit einer ausgewiesenen Managementweiterbildung auf Fachhochschulniveau oder einer vergleich baren Weiterbildung</li>
      <li>Hohe Patientenorientierung</li>
      <li>Konzeptionelle Fähigkeiten verbunden mit Innovationskraft und unternehmerischen Denken und Handeln</li>
      <li>Kommunikative und teamorientierte Persön­lichkeit mit betriebswirtschaftlichen und organisatorischen Fähigkeiten</li>
      <li>Engagement für eine interdisziplinäre und inter­professionelle Zusammenarbeit mit einem hohen Mass an Verantwortungsbereitschaft</li>
    </ul>
  </section>

  <div class="closing">
    <p>Suchen Sie eine verantwortungsvolle Herausforderung in einem familiären, dynamischen Umfeld mit attraktiven Entwicklungsmöglichkeiten?</p>
    <p><strong>Wir garantieren Ihnen absolute Diskretion.</strong></p>
    <p>Für einen ersten vertraulichen Kontakt steht Ihnen Herr <strong>Lukas Brenner</strong> gerne zur Verfügung.<br>
    Zögern Sie nicht, wir freuen uns auf Ihre komplette online Bewerbung mit Foto per E-Mail an:<br>
    <strong>lukas.brenner@valorintgruppe.com</strong></p>
  </div>

  <div class="advisor">
    <h3>Ihr Berater:</h3>
    <p>Lukas Brenner<br>Tel. +41 44 608 27 35<br>Mail: lukas.brenner@valorintgruppe.com<br>Web: valorintgruppe.com</p>
    <p class="social">Finde uns auf SOCIAL MEDIA!</p>
  </div>

  <div class="brand">
    <div class="name"><span class="dot"></span>Valorint Recruitment Group</div>
    <div class="address">Valorint – Recruitment Group Ltd.<br>Lindenweg 14 | CH-6003 Luzern</div>
  </div>

  <div class="page-foot"></div>
</div>
</body>
</html>
```